Website design for labour force (commercial truck driver) company

Looking for a Wordpress template (or design files in conjunction with a free Wordpress template).
Company tag line:
Tenvora – On Demand, Professional Drivers
Real Drivers | Real Standards | Real Results
Logo design has already been completed and is attached

Company provides contract drivers to trucking companies. Target market is both the trucking companies looking for drivers and drivers looking for work.
Design to encompass header / footer and basic page design, navigation menu, home page, contact page. Customer will add content and additional pages over time.

```html
<!DOCTYPE html>
<html lang="en">
<head>
<meta charset="utf-8">
<title>Tenvora – On Demand, Professional Drivers</title>
<link href="https://fonts.googleapis.com/css2?family=Poppins:wght@400;500;600;700;800&display=swap" rel="stylesheet">
<style>
:root{
  --green:#1a7f5a;
  --green-light:#27a373;
  --navy:#0e1624;
  --charcoal:#2c2829;
  --footer:#2a2627;
  --ink:#1b1b1b;
  --muted:#555;
  --paper:#ffffff;
  --mist:#f3f4f6;
  --outline-grey:#9a9a9a;
}
*{box-sizing:border-box;margin:0;padding:0}
html,body{width:1200px;height:4110px;overflow:hidden}
body{font-family:'Poppins',sans-serif;color:var(--ink);background:var(--paper);position:relative}
.abs{position:absolute}
a{color:inherit;text-decoration:none}
.btn{position:absolute;display:flex;align-items:center;justify-content:center;height:42px;border-radius:21px;font-size:11px;font-weight:700;letter-spacing:.3px;text-transform:uppercase}
.btn-green{background:var(--green);color:#fff}
.btn-ghost-light{border:1.5px solid #fff;color:#fff}
.btn-ghost-dark{border:1.5px solid var(--ink);color:var(--ink)}
.btn-white{background:#fff;color:var(--ink)}
.outline{color:transparent;-webkit-text-stroke:1.4px var(--green-light)}
.photo{position:absolute}

/* header */
.site-header{position:absolute;left:0;top:0;width:1200px;height:75px;background:#fff}
.brand{position:absolute;left:90px;top:20px;display:flex;align-items:center;gap:10px;font-size:25px;font-weight:700}
.brand .mark{width:30px;height:30px;border-radius:50%;background:var(--green)}
.nav{position:absolute;left:458px;top:29px;display:flex;gap:30px;font-size:11px;font-weight:600;text-transform:uppercase}
.nav .active{color:var(--green)}
.phone{position:absolute;left:942px;top:19px;display:flex;align-items:center;gap:10px;font-size:15px;font-weight:700}
.phone .ic{width:36px;height:36px;border-radius:50%;background:var(--green);display:flex;align-items:center;justify-content:center}

/* hero */
.hero{position:absolute;left:0;top:75px;width:1200px;height:729px;background:var(--navy)}
.hero-photo{left:470px;top:0;width:730px;height:729px;background:linear-gradient(100deg,#0e1624 0%,#3a4656 20%,#b8474a 48%,#c9d1da 72%,#e8ecf1 100%)}
.hero h1{position:absolute;left:88px;top:140px;font-size:62px;line-height:61px;font-weight:800;color:#fff}
.hero .sub{position:absolute;left:88px;top:398px;font-size:22px;font-weight:500;color:#fff}
.mist{position:absolute;left:0;top:804px;width:1200px;height:503px;background:var(--mist)}

/* about */
.about{position:absolute;left:121px;top:721px;width:958px;height:414px;background:#fff}
.about-photo{left:99px;top:84px;width:400px;height:247px;background:linear-gradient(120deg,#2f5c8c,#5b7fa6 50%,#c06a52)}
.about h2{position:absolute;left:541px;top:99px;font-size:34px;font-weight:700}
.about p{position:absolute;left:541px;top:150px;width:320px;font-size:11px;line-height:17px;color:#333}
.marquee{position:absolute;left:-2px;top:1192px;width:1204px;display:flex;gap:36px;align-items:center;font-size:46px;font-weight:600;white-space:nowrap}
.marquee .outline{-webkit-text-stroke:1.3px var(--outline-grey)}
.marquee .star{color:var(--green);font-size:58px;font-weight:800}

/* why */
.section-title{position:absolute;width:1200px;left:0;text-align:center;font-size:34px;font-weight:700}
.feature{position:absolute;width:240px}
.feature h3{font-size:14px;font-weight:600;margin-bottom:5px}
.feature p{font-size:11px;line-height:17px;color:var(--muted)}
.feature.r{text-align:right}
.ficon{position:absolute;width:56px;height:56px}
.why-photo{left:240px;top:1444px;width:718px;height:506px;background:radial-gradient(ellipse at 50% 60%,#c9cbce 0%,#e6e7e9 45%,rgba(255,255,255,0) 72%)}

/* driver cta */
.driver-cta{position:absolute;left:0;top:1950px;width:1200px;height:404px;background:var(--charcoal)}
.driver-bg{position:absolute;left:0;top:0;width:1200px;height:404px;background:radial-gradient(ellipse at 50% 40%,#353132 0%,var(--charcoal) 70%)}
.driver-cta h2{position:absolute;width:1200px;top:110px;text-align:center;font-size:60px;font-weight:700;color:#fff}
.driver-cta p{position:absolute;left:320px;width:560px;top:197px;text-align:center;font-size:16px;line-height:24px;color:#ddd}
.road{position:absolute;left:0;top:2354px;width:1200px;height:43px;background:#17181b;border-top:4px solid var(--green)}

/* steps */
.step{position:absolute;top:2531px;width:226px}
.step .img{width:226px;height:299px}
.step .num{position:absolute;right:26px;top:22px;width:50px;height:50px;border-radius:50%;border:2px solid #fff;color:#fff;display:flex;align-items:center;justify-content:center;font-size:24px;font-weight:700;background:rgba(0,0,0,.25)}
.step h3{text-align:center;font-size:16px;font-weight:600;margin-top:17px}
.step p{text-align:center;font-size:12px;color:#444;margin-top:2px}

/* testimonial */
.testi-photo{left:80px;top:2921px;width:582px;height:552px;background:linear-gradient(180deg,#f2f3f5 0%,#c9cdd3 45%,#3e4a5c 80%,#2d3a4d 100%)}
.quote{position:absolute;left:690px;top:3130px;width:432px;text-align:center;font-size:26px;line-height:34px;font-weight:600}
.author{position:absolute;left:690px;width:432px;top:3282px;text-align:center;font-size:10px;font-weight:600;text-transform:uppercase}
.arrow{position:absolute;top:3326px;width:44px;height:44px;border-radius:50%;border:1.5px solid var(--ink);display:flex;align-items:center;justify-content:center}

/* green cta */
.cta{position:absolute;left:0;top:3473px;width:1200px;height:258px;background:var(--green)}
.cta h2{position:absolute;width:1200px;top:67px;text-align:center;font-size:33px;font-weight:700;color:#fff}
.cta h2 .outline{-webkit-text-stroke:1.2px #7fd3ad}
.cta p{position:absolute;width:1200px;top:118px;text-align:center;font-size:16px;color:#fff}

/* footer */
.footer{position:absolute;left:0;top:3731px;width:1200px;height:379px;background:var(--footer);color:#fff}
.footer-brand{position:absolute;left:90px;top:122px;display:flex;align-items:center;gap:16px;font-size:52px;font-weight:600}
.footer-brand .mark{width:60px;height:60px;border-radius:50%;background:#fff}
.fcol{position:absolute;top:107px;display:flex;flex-direction:column;gap:10px;font-size:14px}
.fcol a{text-decoration:underline;text-underline-offset:3px}
.finfo{position:absolute;left:956px;top:96px;font-size:11px;line-height:22px}
.finfo h4{font-size:16px;font-weight:600;margin-bottom:8px}
.divider{position:absolute;left:90px;top:304px;width:1020px;height:1px;background:#4a4546}
.copy{position:absolute;left:90px;top:336px;font-size:11px}
.copy span{color:var(--green-light)}
.social{position:absolute;top:326px;display:flex;align-items:center;gap:14px;font-size:10px;color:#bbb}
.social i{width:36px;height:36px;border-radius:50%;background:#3a3536;display:block}
.totop{position:absolute;left:1135px;top:269px;width:42px;height:42px;border-radius:50%;background:var(--green);display:flex;align-items:center;justify-content:center}
</style>
</head>
<body>

<header class="site-header">
  <div class="brand"><span class="mark"></span>Tenvora</div>
  <nav class="nav">
    <a class="active">Home</a><a>Hire a Driver</a><a>Find Driving Jobs</a><a>About Us</a><a>Contact</a>
  </nav>
  <div class="phone">
    <span class="ic"><svg width="16" height="16" viewBox="0 0 24 24" fill="#fff"><path d="M6.6 10.8a15 15 0 0 0 6.6 6.6l2.2-2.2a1 1 0 0 1 1-.25 11.4 11.4 0 0 0 3.6.57 1 1 0 0 1 1 1V20a1 1 0 0 1-1 1A17 17 0 0 1 3 4a1 1 0 0 1 1-1h3.5a1 1 0 0 1 1 1c0 1.25.2 2.45.57 3.57a1 1 0 0 1-.25 1z"/></svg></span>
    (+44) 555 018 274
  </div>
</header>

<section class="hero">
  <div class="photo hero-photo" role="img" aria-label="Smiling truck driver in a plaid shirt giving an OK sign from the cab, trucks parked outside"></div>
  <h1>Professional<br><span class="outline">Drivers</span> When<br>You Need<br>Them</h1>
  <p class="sub">Reliable. Experienced. Ready to Roll.</p>
  <a class="btn btn-green" style="left:88px;top:454px;width:150px">Hire a Driver</a>
  <a class="btn btn-ghost-light" style="left:247px;top:454px;width:150px">Find Driving Jobs</a>
</section>

<div class="mist"></div>

<section class="about">
  <div class="photo about-photo" role="img" aria-label="Two drivers reviewing paperwork on a clipboard beside a truck"></div>
  <svg class="abs" style="left:283px;top:192px" width="34" height="34" viewBox="0 0 34 34"><circle cx="17" cy="17" r="17" fill="#fff"/><path d="M14 11l9 6-9 6z" fill="#1b1b1b"/></svg>
  <h2>About Us</h2>
  <p>At Tenvora, we connect trucking companies with qualified, contract drivers — fast. Whether you're looking to fill a last-minute shift or build a long-term partnership, our experienced drivers are ready to hit the road. We believe in high standards, safety, and results that move your business forward.</p>
  <a class="btn btn-ghost-dark" style="left:541px;top:268px;width:118px">Read More</a>
</section>

<div class="marquee">
  <span class="outline">Real Drivers</span><span class="star">*</span>
  <span class="outline">Real Standards</span><span class="star">*</span>
  <span class="outline">Real Results</span>
</div>

<h2 class="section-title" style="top:1372px">Why Choose Tenvora?</h2>
<div class="photo why-photo" role="img" aria-label="Smiling businesswoman holding a clipboard in front of a silver hatchback car"></div>

<div class="feature r" style="left:148px;top:1451px"><h3>Vetted, Professional Drivers</h3><p>All drivers are background-checked,<br>licensed, and experienced.</p></div>
<svg class="ficon" style="left:400px;top:1450px" viewBox="0 0 56 56" fill="none" stroke="#1a7f5a" stroke-width="2"><circle cx="18" cy="12" r="7"/><path d="M6 48V34a12 12 0 0 1 24 0v14"/><path d="M28 36h16l8 8v6H28z"/><circle cx="34" cy="50" r="3"/><circle cx="47" cy="50" r="3"/></svg>
<div class="feature" style="left:824px;top:1451px"><h3>Nationwide Network</h3><p>Wherever you are, we've got drivers<br>near you.</p></div>
<svg class="ficon" style="left:752px;top:1448px" viewBox="0 0 56 56" fill="none" stroke="#1a7f5a" stroke-width="2"><circle cx="28" cy="28" r="25"/><path d="M3 28h50M28 3c-9 8-9 42 0 50M28 3c9 8 9 42 0 50"/></svg>
<div class="feature r" style="left:148px;top:1561px"><h3>Flexible Contracts</h3><p>On-demand or long-term — we<br>adapt to your needs.</p></div>
<svg class="ficon" style="left:402px;top:1558px" viewBox="0 0 56 56" fill="none" stroke="#1a7f5a" stroke-width="2"><rect x="8" y="6" width="32" height="44" rx="2"/><path d="M16 16h16M16 24h16M16 32h10"/><path d="M36 40l6 6 10-14"/></svg>
<div class="feature" style="left:824px;top:1561px"><h3>Driver Support</h3><p>We support our drivers with 24/7 help,<br>training, and guidance.</p></div>
<svg class="ficon" style="left:752px;top:1558px" viewBox="0 0 56 56" fill="none" stroke="#1a7f5a" stroke-width="2"><circle cx="28" cy="14" r="9"/><path d="M10 52V42a18 18 0 0 1 36 0v10"/><circle cx="28" cy="42" r="8"/></svg>

<section class="driver-cta">
  <div class="driver-bg" role="img" aria-label="Faint aerial view of winding roads in dark charcoal tones"></div>
  <h2>Are You a <span class="outline">Driver?</span></h2>
  <p>Join the Tenvora network and start getting real driving jobs. We connect professional CDL drivers with top-paying opportunities.</p>
  <a class="btn btn-green" style="left:526px;top:270px;width:148px">Apply Now</a>
</section>
<div class="road" role="img" aria-label="Dark road strip with lane markings"></div>

<h2 class="section-title" style="top:2464px">How It Works</h2>
<div class="step" style="left:243px"><div class="photo img" style="position:relative;background:linear-gradient(160deg,#cfd4da,#5c6c86 60%,#2f3c52)" role="img" aria-label="Driver in a car reading job paperwork"><span class="num">1</span></div><h3>Request a Driver</h3><p>Submit your job details</p></div>
<div class="step" style="left:487px"><div class="photo img" style="position:relative;background:linear-gradient(160deg,#a9adb2,#6c6a66 55%,#3a3733)" role="img" aria-label="Smiling driver giving thumbs up from a car window"><span class="num">2</span></div><h3>Get Matched Fast</h3><p>We assign a qualified driver</p></div>
<div class="step" style="left:731px"><div class="photo img" style="position:relative;background:linear-gradient(160deg,#e2e4e6,#9ea3a8 55%,#4b4f55)" role="img" aria-label="Driver talking on the phone behind the wheel"><span class="num">3</span></div><h3>Drive with Confidence</h3><p>Reliable, professional service</p></div>

<div class="photo testi-photo" role="img" aria-label="Bearded truck driver in a cap with arms crossed in front of a white truck"></div>
<svg class="abs" style="left:840px;top:3022px" width="132" height="86" viewBox="0 0 132 86" fill="#1a7f5a"><path d="M30 86a30 30 0 1 1 28-40C60 20 50 4 32 0c22 2 34 22 30 50a32 32 0 0 1-32 36z"/><path d="M100 86a30 30 0 1 1 28-40C130 20 120 4 102 0c22 2 34 22 30 50a32 32 0 0 1-32 36z"/></svg>
<p class="quote">"I joined Tenvora and found consistent work within a week. Highly recommend to any driver."</p>
<p class="author">— Daniel K., CDL Class A Driver</p>
<div class="arrow" style="left:857px"><svg width="12" height="12" viewBox="0 0 12 12"><path d="M8 2L4 6l4 4" stroke="#1b1b1b" stroke-width="1.6" fill="none"/></svg></div>
<div class="arrow" style="left:910px"><svg width="12" height="12" viewBox="0 0 12 12"><path d="M4 2l4 4-4 4" stroke="#1b1b1b" stroke-width="1.6" fill="none"/></svg></div>

<section class="cta">
  <h2>Ready to <span class="outline">Drive</span> your Business Forward?</h2>
  <p>Let Tenvora provide the talent you need.</p>
  <a class="btn btn-white" style="left:469px;top:156px;width:127px">Hire a Driver</a>
  <a class="btn btn-ghost-light" style="left:604px;top:156px;width:127px">Apply to Drive</a>
</section>

<footer class="footer">
  <div class="footer-brand"><span class="mark"></span>Tenvora</div>
  <div class="fcol" style="left:586px"><a>Hire a Driver</a><a>Find Driving Jobs</a><a>About Us</a><a>Contact</a></div>
  <div class="fcol" style="left:779px"><a>Legal notices</a><a>Terms &amp; Condition</a><a>Privacy policy</a><a>Contact</a></div>
  <div class="finfo"><h4>Tenvora</h4>Some address goes here<br>Mobile: +44 555 018 274<br>Email: info@tenvora.com</div>
  <div class="divider"></div>
  <p class="copy">© 2025 <span>Tenvora</span> - All rights reserved</p>
  <div class="social" style="left:769px"><i></i>Community</div>
  <div class="social" style="left:911px"><i></i>Updates</div>
  <div class="social" style="left:1029px"><i></i>Network</div>
  <div class="totop"><svg width="14" height="14" viewBox="0 0 14 14"><path d="M7 12V2M3 6l4-4 4 4" stroke="#fff" stroke-width="1.6" fill="none"/></svg></div>
</footer>

</body>
</html>
```